Stationary Package
Business Card / Letterhead / Envelop
I need double sided standard sized Business Card [3.5" x 2"]
use same look and feel font(s)
Professional
Daniel Whitfield
Marketing Strategist
4518 Harwick Crescent
Mississauga, Ontario, L4T 3K8
danielwhitfield@vellorahaus.com
www.vellorahaus.com
design package for the marketing industry
Logo with tag line
plus the website address
Logo and Tag Line
eps logo
pdf logo version

```html
<!DOCTYPE html>
<html lang="en">
<head>
<meta charset="utf-8">
<title>Daniel Whitfield – Business Card</title>
<link rel="stylesheet" href="https://fonts.googleapis.com/css2?family=Archivo:wght@800&family=Open+Sans:wght@400;600;700&display=swap">
<style>
  :root {
    --page-bg: #eceae6;
    --card-bg: #ffffff;
    --brand-blue: #1f6fc0;
    --deep-blue: #0f4f9a;
    --stripe-black: #0b0b0b;
    --ink: #1c1c1c;
    --ink-soft: #4a4a4a;
  }
  * { margin: 0; padding: 0; box-sizing: border-box; }
  html, body {
    width: 1200px; height: 935px; overflow: hidden;
    background: var(--page-bg);
  }
  .business-card {
    position: absolute; left: 190px; top: 232px;
    width: 820px; height: 470px;
    background: var(--card-bg);
    border-radius: 38px;
    overflow: hidden;
    box-shadow: 0 6px 18px rgba(0,0,0,0.18);
    font-family: "Open Sans", Arial, sans-serif;
  }
  .card-swooshes { position: absolute; inset: 0; }
  .brand-block {
    position: absolute; left: 64px; top: 142px; width: 400px;
    text-align: center;
  }
  .brand-dot {
    width: 112px; height: 112px; border-radius: 50%;
    background: var(--brand-blue);
    margin: 0 auto 22px;
  }
  .brand-name {
    font-family: "Archivo", "Arial Black", sans-serif;
    font-weight: 800; font-size: 37px; line-height: 1;
    color: var(--brand-blue); letter-spacing: 0.5px;
    white-space: nowrap;
  }
  .brand-tagline {
    font-size: 22px; color: var(--ink); margin-top: 6px; margin-left: -60px;
  }
  .contact-block {
    position: absolute; left: 497px; top: 104px;
    color: var(--ink-soft); font-size: 20px; line-height: 28px;
  }
  .person-name { font-weight: 700; font-size: 29px; line-height: 34px; color: var(--ink); }
  .person-title { font-size: 18px; line-height: 24px; color: var(--brand-blue); margin-bottom: 24px; }
  .contact-label { color: var(--deep-blue); font-weight: 700; }
</style>
</head>
<body>
  <div class="business-card">
    <svg class="card-swooshes" width="820" height="470" viewBox="0 0 820 470">
      <defs>
        <linearGradient id="blueFade" x1="0" y1="0" x2="1" y2="1">
          <stop offset="0" stop-color="#3b8fe0"/>
          <stop offset="1" stop-color="#0f4f9a"/>
        </linearGradient>
      </defs>
      <path d="M0,184 C20,320 110,430 243,470 L0,470 Z" fill="var(--stripe-black)"/>
      <path d="M0,261 C25,360 90,440 166,470 L0,470 Z" fill="url(#blueFade)"/>
      <path d="M660,0 C760,60 812,200 820,376 L820,0 Z" fill="var(--stripe-black)"/>
      <path d="M712,0 C790,50 815,170 820,325 L820,0 Z" fill="url(#blueFade)"/>
    </svg>

    <div class="brand-block">
      <div class="brand-dot"></div>
      <div class="brand-name">DANIEL WHITFIELD</div>
      <div class="brand-tagline">Vellora Haus</div>
    </div>

    <div class="contact-block">
      <div class="person-name">Daniel Whitfield</div>
      <div class="person-title">Marketing Strategist</div>
      <div>4518 Harwick Crescent</div>
      <div>Mississauga, ON L4T 3K8</div>
      <div><span class="contact-label">Phone :</span> 905-555-0142</div>
      <div><span class="contact-label">Cell :</span> 905-555-0178</div>
      <div><span class="contact-label">Fax :</span> 905-555-0146</div>
      <div><span class="contact-label">Email :</span> danielwhitfield@vellorahaus.com</div>
    </div>
  </div>
</body>
</html>
```